Looking for business card/letterhead/email signature

Take existing logo and create full design suite of collateral

Contact Information for Business Card

Use mock details that can be edited by us

Font styles to use
Sans Serif

```html
<!DOCTYPE html>
<html lang="en">
<head>
<meta charset="utf-8">
<title>Harlow Digital – Stationery Suite</title>
<link href="https://fonts.googleapis.com/css2?family=Poppins:wght@300;400;700&family=Roboto:wght@400;500;700&display=swap" rel="stylesheet">
<style>
  :root{
    --bg:#e3e3e3;
    --paper:#ffffff;
    --brand:#0a4d92;
    --brand-dark:#083f78;
    --accent:#e4197b;
    --ink:#3d3d3d;
    --ink-soft:#6a6a6a;
    --rule:#c9c9c9;
    --sig:#eef1f8;
  }
  *{box-sizing:border-box;margin:0;padding:0}
  html,body{width:1200px;height:738px;overflow:hidden;background:var(--bg)}
  body{position:relative;font-family:'Roboto',Arial,sans-serif;color:var(--ink)}
  .sheet{position:absolute;background:var(--paper);box-shadow:0 1px 4px rgba(0,0,0,.18)}

  /* wordmark */
  .wordmark{position:absolute;display:flex;align-items:center;gap:3px;font-family:'Poppins',Arial,sans-serif;font-weight:700;color:var(--brand);letter-spacing:-.5px;line-height:1}
  .wordmark .dot{border-radius:50%;background:var(--accent);flex:none}
  .wordmark.on-dark{color:#fff}

  /* letterhead */
  .letterhead{left:66px;top:74px;width:452px;height:583px}
  .letterhead .wordmark{left:40px;top:58px;font-size:24px}
  .letterhead .wordmark .dot{width:9px;height:9px}
  .lh-contact{position:absolute;top:57px;left:230px;display:flex;font-size:6.2px;line-height:8px;color:var(--ink-soft)}
  .lh-contact .addr{text-align:right;padding-right:6px;border-right:.8px solid var(--rule)}
  .lh-contact .addr b{font-weight:500;color:var(--ink)}
  .lh-contact .lines{padding-left:6px}
  .icon-row{display:flex;align-items:center;gap:3px}
  .icon-row svg{width:5px;height:5px;fill:var(--brand);flex:none}
  .salutation{position:absolute;left:40px;top:169px;font-family:'Poppins',Arial,sans-serif;font-weight:300;font-size:11.5px;color:var(--ink)}
  .letter-body{position:absolute;left:40px;top:204px;width:374px;font-family:'Poppins',Arial,sans-serif;font-weight:300;font-size:6.3px;line-height:9.6px;color:var(--ink-soft)}
  .letter-body p{margin-bottom:9.6px}
  .signoff{position:absolute;left:40px;top:406px;font-family:'Poppins',Arial,sans-serif;font-weight:300;font-size:6.3px;color:var(--ink-soft)}
  .signature{position:absolute;left:38px;top:432px;width:82px;height:34px;background:var(--sig);border-radius:3px}

  /* business cards */
  .card{width:250px;height:143px}
  .card-front{left:593px;top:115px}
  .card-front .wordmark{left:26px;top:58px;font-size:26px}
  .card-front .wordmark .dot{width:9px;height:9px}
  .card-front .divider{position:absolute;left:133px;top:33px;width:.8px;height:80px;background:var(--rule)}
  .card-info{position:absolute;left:147px;top:34px;font-size:6.3px;line-height:8px;color:var(--ink-soft)}
  .card-info .name{font-family:'Roboto',Arial,sans-serif;font-weight:700;font-size:9px;line-height:10px;color:var(--brand)}
  .card-info .role{font-weight:500;font-size:6.5px;color:var(--ink);margin-bottom:4px}
  .card-info .co{font-weight:500;color:var(--ink)}
  .card-info .addr{margin-bottom:3px}
  .card-back{left:865px;top:115px;background:var(--brand)}
  .card-back .wordmark{left:78px;top:57px;font-size:27px}
  .card-back .wordmark .dot{width:9px;height:9px}

  /* envelopes */
  .envelope-back{left:601px;top:310px;width:530px;height:231px}
  .flap{position:absolute;left:0;top:0;width:530px;height:78px}
  .envelope-back .wordmark{left:226px;top:32px;font-size:18px}
  .envelope-back .wordmark .dot{width:7px;height:7px}
  .envelope-front{left:549px;top:426px;width:530px;height:231px}
  .envelope-front .wordmark{left:28px;top:46px;font-size:22px}
  .envelope-front .wordmark .dot{width:8px;height:8px}
  .env-addr{position:absolute;left:28px;top:92px;font-size:6.2px;line-height:8px;color:var(--ink-soft)}
  .env-addr b{font-weight:500;color:var(--ink)}
</style>
</head>
<body>

<svg width="0" height="0" style="position:absolute" aria-hidden="true">
  <defs>
    <symbol id="i-phone" viewBox="0 0 10 10"><path d="M2 0.5l2 2-1 1.3c.6 1.3 1.7 2.4 3 3l1.3-1 2 2-1.3 1.7C4 9.2 .6 5.8.3 1.8z"/></symbol>
    <symbol id="i-mobile" viewBox="0 0 10 10"><path d="M2.5 0h5v10h-5zM3.5 1v7h3V1z"/></symbol>
    <symbol id="i-mail" viewBox="0 0 10 10"><path d="M0 2h10v6H0zM1 3l4 2.6L9 3z" fill-rule="evenodd"/></symbol>
    <symbol id="i-web" viewBox="0 0 10 10"><circle cx="5" cy="5" r="5"/></symbol>
  </defs>
</svg>

<!-- Letterhead -->
<section class="sheet letterhead">
  <div class="wordmark">harlow<span class="dot"></span></div>
  <div class="lh-contact">
    <div class="addr"><b>Harlow Digital</b><br>4120 Juniper Court<br>Fairbanks, Alaska 34510</div>
    <div class="lines">
      <div class="icon-row"><svg><use href="#i-phone"/></svg>555 014 2290</div>
      <div class="icon-row"><svg><use href="#i-mail"/></svg>hello@harlowdigital.com</div>
      <div class="icon-row"><svg><use href="#i-web"/></svg>www.harlowdigital.com</div>
    </div>
  </div>
  <p class="salutation">Dear Mr. Reyes,</p>
  <div class="letter-body">
    <p>Lorem ipsum dolor sit amet, consectetur adipiscing elit. Donec orci purus, luctus vitae dignissim eu, iaculis sed purus. Vivamus faucibus, ipsum nec aliquet viverra, leo mauris condimentum ligula, sit amet sagittis enim ligula quis arcu. Nam egestas tortor id nisi porttitor mattis. In tortor ante, ultricies in suscipit a, tempus non massa. Vivamus et auctor mi. Fusce vel massa nulla. Phasellus nec eros mauris, et scelerisque orci.</p>
    <p>Donec malesuada orci vitae nulla accumsan porta a id massa. Quisque accumsan iaculis magna sit amet fringilla. Maecenas consequat, magna eget tincidunt semper, odio nibh rutrum mi, id feugiat ante nisi eu risus. Vestibulum nunc orci, rhoncus a placerat in, ultricies in mi. Cras mattis varius eros, vel fringilla nisi suscipit eget. Quisque scelerisque sagittis nulla at porttitor.</p>
    <p>Sed id augue vitae urna euismod commodo aliquet a quam. Pellentesque arcu velit, cursus et malesuada ut, consequat et diam. Nullam erat sem, rhoncus id ullamcorper vitae, rhoncus et arcu. In ultricies ultricies nulla, ut rutrum nisi iaculis at. Donec eu magna a metus ornare faucibus. Fusce aliquet faucibus ultricies. Morbi semper, est id tincidunt gravida, sem arcu adipiscing lacus, ac bibendum nulla leo eu purus. Quisque nec diam sed risus consectetur a accumsan quis quis nibh. Vestibulum id purus lorem.</p>
    <p>It is a long established fact that a reader will be distracted by the readable content of a page when looking at its layout. The point of using Lorem Ipsum is that it has a more-or-less normal distribution of letters, as opposed to using 'Content here, content here', making it look like readable English. Many desktop publishing packages</p>
  </div>
  <p class="signoff">Sincerely,</p>
  <div class="signature" role="img" aria-label="Handwritten signature of Daniel Reyes"></div>
</section>

<!-- Business card front -->
<section class="sheet card card-front">
  <div class="wordmark">harlow<span class="dot"></span></div>
  <div class="divider"></div>
  <div class="card-info">
    <div class="name">DANIEL REYES</div>
    <div class="role">CEO/FOUNDER</div>
    <div class="addr"><span class="co">Harlow Digital</span><br>4120 Juniper Court<br>Fairbanks, Alaska 34510</div>
    <div class="icon-row"><svg><use href="#i-phone"/></svg>555 014 2290</div>
    <div class="icon-row"><svg><use href="#i-mobile"/></svg>555 017 8843</div>
    <div class="icon-row"><svg><use href="#i-mail"/></svg>daniel@harlowdigital.com</div>
    <div class="icon-row"><svg><use href="#i-web"/></svg>www.harlowdigital.com</div>
  </div>
</section>

<!-- Business card back -->
<section class="sheet card card-back">
  <div class="wordmark on-dark">harlow<span class="dot"></span></div>
</section>

<!-- Envelope back -->
<section class="sheet envelope-back">
  <svg class="flap" viewBox="0 0 530 78" preserveAspectRatio="none" aria-hidden="true">
    <path d="M0 0H530L517 70Q516 77 505 77H25Q13 77 12 70Z" fill="var(--brand)"/>
  </svg>
  <div class="wordmark on-dark">harlow<span class="dot"></span></div>
</section>

<!-- Envelope front -->
<section class="sheet envelope-front">
  <div class="wordmark">harlow<span class="dot"></span></div>
  <div class="env-addr"><b>Harlow Digital</b><br>4120 Juniper Court<br>Fairbanks, Alaska 34510</div>
</section>

</body>
</html>
```